Redesign Business Cards, Attached

Please read instructions carefully. If you have any questions send a message before submitting your ONE design. Please redesign attached business cards. Double sided. Use same content and descriptions. Use black, silver, crimson red and gold colors. My only issue with the attached design is the background colors. I like the layout as-is. I can provide the individual pictures on the back side later. Do not submit more than one design. One submission shall include both front and back. Do not submit front and back separately. A second project will be launched to create a matching post card after completion of this.
Industry/Entity Type
see description and attachments.
Contact Information for Business Card
Requirements
Must have
- see description and attachments.
Nice to have
Should not have

```html
<!DOCTYPE html>
<html lang="en">
<head>
<meta charset="utf-8">
<title>Hollis Boat Training – Business Card</title>
<link href="https://fonts.googleapis.com/css2?family=Montserrat:wght@400;600;700&family=Open+Sans:ital,wght@1,600;1,700&display=swap" rel="stylesheet">
<style>
  :root{
    --stage:#cfcfcf;
    --ink:#0b0b0b;
    --crimson:#9b1626;
    --crimson-deep:#4a0a12;
    --gold:#c9a24a;
    --gold-light:#e3c781;
    --silver:#bdbdbd;
    --silver-light:#d6d6d6;
    --paper:#ffffff;
    --sea-deep:#2f4f72;
    --sea-light:#a9c2dc;
  }
  html,body{margin:0;padding:0;width:1200px;height:390px;overflow:hidden;background:var(--stage);}
  .card{position:absolute;top:62px;width:464px;height:265px;display:block;}
  .card--front{left:111px;}
  .card--back{left:625px;}
  .sans{font-family:"Montserrat",Arial,sans-serif;}
  .tile-label{font-family:"Open Sans",Arial,sans-serif;font-style:italic;font-weight:700;font-size:23px;text-anchor:middle;}
  .tile-label--gold{fill:var(--gold-light);}
  .tile-label--light{fill:var(--paper);}
</style>
</head>
<body>

<!-- Front -->
<svg class="card card--front" viewBox="0 0 996 568" xmlns="http://www.w3.org/2000/svg" aria-label="Business card front">
  <defs>
    <linearGradient id="front-water" x1="0" y1="0" x2="1" y2="1">
      <stop offset="0" stop-color="#111111"/>
      <stop offset="0.55" stop-color="var(--crimson-deep)"/>
      <stop offset="1" stop-color="var(--crimson)"/>
    </linearGradient>
    <linearGradient id="panel-silver" x1="0" y1="0" x2="1" y2="1">
      <stop offset="0" stop-color="var(--silver-light)"/>
      <stop offset="1" stop-color="var(--silver)"/>
    </linearGradient>
  </defs>
  <rect class="front-photo" role="img" aria-label="Darkened aerial photo of a boat on open water" x="0" y="0" width="996" height="568" fill="url(#front-water)"/>
  <polyline class="chevron-band" points="518,0 408,284 518,568" fill="none" stroke="var(--gold)" stroke-width="38"/>
  <polygon class="info-panel" points="560,0 996,0 996,568 560,568 432,284" fill="url(#panel-silver)"/>

  <g class="brand-mark">
    <circle cx="217" cy="284" r="125" fill="var(--gold)"/>
    <text class="sans" x="217" y="276" text-anchor="middle" font-weight="700" font-size="30" fill="var(--ink)">HOLLIS BOAT</text>
    <text class="sans" x="217" y="314" text-anchor="middle" font-weight="700" font-size="30" fill="var(--ink)">TRAINING</text>
  </g>

  <g class="contact">
    <text class="sans" x="556" y="180" font-weight="700" font-size="39" fill="var(--ink)">DANIEL R. HOLLIS</text>
    <text class="sans" x="556" y="214" font-weight="400" font-size="28" fill="var(--crimson)">USCG Licensed Captain</text>
    <text class="sans" x="556" y="248" font-weight="400" font-size="28" fill="var(--ink)">Certified instructor</text>

    <rect class="text-pill" x="556" y="302" width="350" height="54" rx="18" fill="var(--crimson)"/>
    <text class="sans" x="575" y="340" font-weight="600" font-size="27" fill="var(--paper)">TEXT</text>
    <g class="icon-phone" fill="none" stroke="var(--gold-light)" stroke-width="3" stroke-linecap="round">
      <path d="M667 316 q-6 6 0 18 q8 14 20 18 q6 2 10-4 l-6-6 q-4 3-8 0 q-6-5-9-11 q-1-4 3-6 z"/>
      <path d="M686 318 q8 2 10 10"/>
      <path d="M688 310 q14 3 16 18"/>
    </g>
    <text class="sans" x="710" y="339" font-weight="600" font-size="26" fill="var(--paper)">(555) 014-2276</text>

    <g class="icon-mail" fill="none" stroke="var(--crimson)" stroke-width="2.5">
      <rect x="560" y="383" width="22" height="16" rx="2"/>
      <path d="M560 385 l11 8 l11-8"/>
    </g>
    <text class="sans" x="596" y="399" font-weight="400" font-size="22" fill="var(--ink)">hello@harborhelmsman.com</text>

    <g class="icon-globe" fill="none" stroke="var(--crimson)" stroke-width="2.5">
      <circle cx="571" cy="434" r="11"/>
      <ellipse cx="571" cy="434" rx="5" ry="11"/>
      <line x1="560" y1="434" x2="582" y2="434"/>
    </g>
    <text class="sans" x="596" y="441" font-weight="400" font-size="22" fill="var(--ink)">www.HarborHelmsman.com</text>
  </g>
</svg>

<!-- Back -->
<svg class="card card--back" viewBox="0 0 996 568" xmlns="http://www.w3.org/2000/svg" aria-label="Business card back">
  <defs>
    <linearGradient id="back-dark" x1="0" y1="0" x2="1" y2="1">
      <stop offset="0" stop-color="#111111"/>
      <stop offset="0.6" stop-color="var(--crimson-deep)"/>
      <stop offset="1" stop-color="var(--crimson)"/>
    </linearGradient>
    <linearGradient id="back-sea" x1="0" y1="0" x2="1" y2="1">
      <stop offset="0" stop-color="var(--sea-deep)"/>
      <stop offset="1" stop-color="var(--sea-light)"/>
    </linearGradient>
  </defs>
  <rect x="0" y="0" width="996" height="568" fill="var(--paper)"/>
  <rect class="back-dark-photo" role="img" aria-label="Darkened photo of open water" x="0" y="0" width="600" height="321" fill="url(#back-dark)"/>
  <polygon class="chevron-notch" points="529,0 572,0 548,42 510,42" fill="var(--gold)"/>
  <polygon class="boat-photo" role="img" aria-label="Photo of a white motorboat cruising across sparkling blue water" points="579,0 996,0 996,321 579,321 482,156" fill="url(#back-sea)"/>

  <g class="brand-mark">
    <circle cx="261" cy="133" r="94" fill="var(--gold)"/>
    <text class="sans" x="261" y="128" text-anchor="middle" font-weight="700" font-size="23" fill="var(--ink)">HOLLIS BOAT</text>
    <text class="sans" x="261" y="157" text-anchor="middle" font-weight="700" font-size="23" fill="var(--ink)">TRAINING</text>
  </g>

  <g class="services">
    <polygon points="142,263 329,263 289,373 112,373" fill="var(--ink)"/>
    <polygon points="339,263 527,263 487,373 309,373" fill="var(--crimson)"/>
    <polygon points="537,263 724,263 684,373 507,373" fill="var(--ink)"/>
    <polygon points="734,263 924,263 884,373 704,373" fill="var(--crimson)"/>

    <polygon points="109,382 289,382 252,492 72,492" fill="var(--crimson)"/>
    <polygon points="306,382 489,382 452,492 269,492" fill="var(--ink)"/>
    <polygon points="506,382 686,382 649,492 469,492" fill="var(--crimson)"/>
    <polygon points="703,382 886,382 849,492 666,492" fill="var(--ink)"/>

    <text class="tile-label tile-label--gold"><tspan x="220" y="298">Hands-On</tspan><tspan x="220" y="324">Boat</tspan><tspan x="220" y="350">Training</tspan></text>
    <text class="tile-label tile-label--light"><tspan x="418" y="298">Introduction</tspan><tspan x="420" y="324">to Power</tspan><tspan x="422" y="350">boating</tspan></text>
    <text class="tile-label tile-label--gold"><tspan x="616" y="298">Precision</tspan><tspan x="616" y="324">Docking &amp;</tspan><tspan x="616" y="350" textLength="160" lengthAdjust="spacingAndGlyphs">Boat Handling</tspan></text>
    <text class="tile-label tile-label--light"><tspan x="814" y="298">Open Water</tspan><tspan x="814" y="324">Boat</tspan><tspan x="814" y="350">Handling</tspan></text>

    <text class="tile-label tile-label--light"><tspan x="181" y="430">Island</tspan><tspan x="181" y="456">Anchoring</tspan></text>
    <text class="tile-label tile-label--gold"><tspan x="380" y="422">Open Water</tspan><tspan x="380" y="446">Advanced</tspan><tspan x="380" y="470">Maneuvers</tspan></text>
    <text class="tile-label tile-label--light"><tspan x="578" y="430">Coastal</tspan><tspan x="578" y="456">Navigation</tspan></text>
    <text class="tile-label tile-label--gold"><tspan x="774" y="418">Captaining /</tspan><tspan x="770" y="444" textLength="170" lengthAdjust="spacingAndGlyphs">Piloting Service</tspan><tspan x="768" y="469" textLength="172" lengthAdjust="spacingAndGlyphs">for Your Outings</tspan></text>
  </g>

  <text class="sans" x="499" y="541" text-anchor="middle" font-weight="700" font-size="29" fill="var(--ink)">www.HarborHelmsman.com</text>
</svg>

</body>
</html>
```